Orchard of Veloria - Digital Party Invite

I'm throwing a Halloween party with the theme "Orchard of Veloria". The invite will be sent via Quillbright Mail. I need a custom design for the invite. Here are the details:
The image needs to be 670x970.
Needs to be sexy - maybe with Adam & Eve, and the snake w/the apple, etc
Text should be:
You Are Invited To
The Orchard of Veloria
Sat Oct 26 7:00PM
at
Marta & Lucio's Home
527 Harlow Crest Rd 7B
Costumes Highly Encouraged
Adults Only Please

```html
<!DOCTYPE html>
<html lang="en">
<head>
<meta charset="utf-8">
<title>Orchard of Veloria – Party Invite</title>
<link rel="stylesheet" href="https://fonts.googleapis.com/css2?family=Montserrat:wght@600&family=Fraunces:opsz,wght,SOFT@144,600,100&family=Tinos&family=Cinzel:wght@500&display=swap">
<style>
  :root {
    --stage: #cfcfcf;
    --paper: #f9fbfd;
    --frame: #f5c27a;
    --ink: #111111;
    --rose: #e9879f;
    --lavender: #978bc6;
    --leaf: #5f9a52;
    --leaf-wash: rgba(120, 180, 105, .5);
    --leaf-deep: rgba(95, 154, 82, .5);
    --blush-wash: rgba(242, 167, 169, .55);
    --lavender-wash: rgba(151, 139, 198, .45);
  }
  * { margin: 0; padding: 0; box-sizing: border-box; }
  html, body { width: 915px; height: 1200px; overflow: hidden; background: var(--stage); }
  .invite {
    position: absolute; left: 107px; top: 93px; width: 702px; height: 1014px;
    background: var(--paper); overflow: hidden;
  }
  .floral { position: absolute; }
  .floral--top-right {
    left: 242px; top: 0; width: 460px; height: 200px;
    background: radial-gradient(ellipse farthest-side at 100% 0%,
      var(--leaf-wash) 0%, var(--blush-wash) 45%, rgba(140,192,122,.3) 75%, rgba(140,192,122,0) 100%);
  }
  .floral--right-edge {
    left: 580px; top: 200px; width: 122px; height: 210px;
    background: radial-gradient(ellipse farthest-side at 100% 50%,
      var(--leaf-wash) 0%, var(--lavender-wash) 50%, rgba(151,139,198,0) 100%);
  }
  .floral--left-edge {
    left: 0; top: 410px; width: 200px; height: 370px;
    background: radial-gradient(ellipse farthest-side at 0% 50%,
      var(--leaf-wash) 0%, var(--lavender-wash) 55%, rgba(151,139,198,0) 100%);
  }
  .floral--bottom {
    left: 0; top: 790px; width: 580px; height: 224px;
    background: radial-gradient(ellipse farthest-side at 25% 100%,
      var(--leaf-deep) 0%, var(--blush-wash) 50%, rgba(140,192,122,.3) 78%, rgba(140,192,122,0) 100%);
  }
  .frame { position: absolute; left: 0; top: 0; width: 702px; height: 1014px; }
  .copy { position: absolute; left: 0; width: 702px; text-align: center; white-space: nowrap; }
  .kicker {
    top: 229px; font: 600 21px/1 "Montserrat", sans-serif; color: var(--ink); letter-spacing: .3px;
  }
  .title {
    font-family: "Fraunces", serif; font-weight: 600;
    font-variation-settings: "SOFT" 100, "opsz" 144; letter-spacing: -2px; line-height: 1;
  }
  .title--line1 { top: 257px; font-size: 64px; color: var(--rose); }
  .title--line2 { top: 323px; font-size: 64px; color: var(--lavender); }
  .date { position: absolute; top: 438px; left: 0; width: 702px; height: 70px; font-family: "Tinos", serif; }
  .date__month, .date__year { position: absolute; top: 14px; font-size: 37px; line-height: 1; color: var(--ink); }
  .date__month { left: 256px; }
  .date__year { left: 409px; }
  .date__day { position: absolute; left: 310px; width: 90px; top: -4px; text-align: center; font-size: 66px; line-height: 1; color: var(--rose); }
  .date__time { position: absolute; left: 300px; width: 110px; top: 50px; text-align: center; font-size: 17px; line-height: 1; color: var(--ink); }
  .date__rule { position: absolute; top: 3px; width: 2px; height: 62px; background: var(--lavender); }
  .date__rule--left { left: 308px; }
  .date__rule--right { left: 400px; }
  .venue { font: 500 23px/25px "Cinzel", serif; color: var(--ink); }
  .venue--host { top: 551px; }
  .venue--street { top: 576px; }
  .notes { font: 500 17px/19px "Cinzel", serif; color: var(--leaf); }
  .notes--costume { top: 648px; }
  .notes--adults { top: 667px; }
</style>
</head>
<body>
<main class="invite">
  <div class="floral floral--top-right" role="img" aria-label="Watercolour roses, bellflowers and leaves spilling from the top right corner"></div>
  <div class="floral floral--right-edge" role="img" aria-label="Trailing purple bellflower, rosebud and leaf along the right edge"></div>
  <div class="floral floral--left-edge" role="img" aria-label="Climbing leaves, pink buds and purple bellflowers on the left side"></div>
  <div class="floral floral--bottom" role="img" aria-label="Watercolour pink roses and green foliage along the bottom"></div>

  <svg class="frame" viewBox="0 0 702 1014" aria-hidden="true">
    <g fill="none" stroke="var(--frame)" stroke-width="3">
      <rect x="58" y="73" width="570" height="849"/>
      <path d="M74 141 V93 H139 M242 93 H644 V650 M644 722 V942 H118 M74 176 V238 M74 283 V700"/>
      <path d="M118 922 H475 M524 922 H610"/>
    </g>
  </svg>

  <p class="copy kicker">YOU ARE INVITED TO</p>
  <h1 class="copy title title--line1">The Orchard</h1>
  <h1 class="copy title title--line2">of Veloria</h1>

  <div class="date">
    <span class="date__month">10</span>
    <span class="date__rule date__rule--left"></span>
    <span class="date__day">26</span>
    <span class="date__time">7:00 PM</span>
    <span class="date__rule date__rule--right"></span>
    <span class="date__year">24</span>
  </div>

  <p class="copy venue venue--host">Marta &amp; Lucio's Home</p>
  <p class="copy venue venue--street">527 Harlow Crest Rd 7B</p>

  <p class="copy notes notes--costume">Costumes Highly Encouraged</p>
  <p class="copy notes notes--adults">Adults Only Please</p>
</main>
</body>
</html>
```